Quorvex clinic business card - double sided for young clinic

I require business cards for my aesthetic clinic specialising in the below treatments. I would like the cards to be modern as my clinic base are young 22-35 years old. I require my logo on it and would like the edges to be rounded.

I have an aesthetic clinic specialising in :
Quorvex
Lip Enhancement
Chemical Peels
Facial Fillers
Non Surgical Face Lift

I would the cards to have the following information on them:
My logo - (in grey/silver)
address
Phone number
services

Colours :
White/grey/silver and red

a nice image on there, perhaps a set of lips as this is a main service i deliver

Company Name: PDA Address: 52 Farrowmere Road, 4 Brackwell High Street, KT9 4WQ Phone: 0208 794 2160 Website: www.penningtondoweaesthetics.co.uk

Target Market(s)

clinics 22-45 years old mainly female

Industry/Entity Type

Business

Contact Information for Business Card

as above

Requirements
Must have
• logo
• Address
• Email
• Phone number
• Services i offer
Nice to have
• images

```html
<!DOCTYPE html>
<html lang="en">
<head>
<meta charset="utf-8">
<title>PDA Business Card</title>
<link rel="stylesheet" href="https://fonts.googleapis.com/css2?family=Crimson+Pro:wght@500;600&display=swap">
<style>
  :root {
    --page: #ffffff;
    --card: #e2e2e2;
    --ink: #3a3a3a;
    --silver: #9c9da0;
    --web: #a7a8aa;
    --accent: #d8323c;
    --photo-light: #d9d9d9;
    --photo-mid: #8a8480;
    --photo-dark: #4a3a34;
  }
  * { margin: 0; padding: 0; box-sizing: border-box; }
  html, body { width: 846px; height: 1200px; overflow: hidden; background: var(--page); }
  body { position: relative; font-family: "Crimson Pro", Georgia, serif; }

  .card {
    position: absolute;
    width: 686px;
    height: 444px;
    background: var(--card);
    border-radius: 36px;
    box-shadow: 4px 6px 7px rgba(0, 0, 0, 0.35);
  }
  .card--front { left: 82px; top: 94px; }
  .card--back { left: 102px; top: 661px; }

  .accent-rule {
    position: absolute;
    height: 3px;
    background: var(--accent);
  }

  .brand {
    position: absolute;
    left: 0; right: 0; top: 72px;
    text-align: center;
    color: var(--silver);
    font-weight: 500;
    letter-spacing: 0.12em;
  }
  .brand__mark {
    display: block;
    width: 58px; height: 58px;
    margin: 0 auto 20px;
    border-radius: 50%;
    background: var(--silver);
  }
  .brand__name { display: block; font-size: 21px; line-height: 20px; }
  .brand__tag { display: block; font-size: 30px; line-height: 28px; }

  .contact {
    position: absolute;
    left: 0; right: 0; top: 287px;
    text-align: center;
    color: var(--ink);
    font-weight: 600;
    font-size: 22px;
    line-height: 35px;
  }
  .contact__web { color: var(--web); }

  .treatment-photo {
    position: absolute;
    left: 207px; top: 59px;
    width: 270px; height: 264px;
    background: radial-gradient(ellipse at 50% 40%, var(--photo-dark) 0%, var(--photo-mid) 35%, var(--photo-light) 80%, var(--card) 100%);
  }

  .services {
    position: absolute;
    left: 0; right: 0; top: 324px;
    text-align: center;
    color: var(--ink);
    font-weight: 600;
    font-size: 22px;
    line-height: 36px;
    letter-spacing: 0.01em;
  }
  .services .sep { color: var(--silver); font-weight: 500; margin: 0 8px; }
</style>
</head>
<body>

<section class="card card--front">
  <div class="accent-rule" style="left:0; width:85px; top:133px;"></div>
  <div class="accent-rule" style="left:600px; width:86px; top:133px;"></div>

  <div class="brand">
    <span class="brand__mark"></span>
    <span class="brand__name">PENNINGTON DOWE</span>
    <span class="brand__tag">AESTHETICS</span>
  </div>

  <div class="accent-rule" style="left:87px; width:511px; top:276px;"></div>

  <div class="contact">
    <p>020 8794 2160 | pdabrackwellbookings@mailbox.co.uk</p>
    <p>4 Brackwell Parade, Surrey, KT9 4WQ</p>
    <p class="contact__web">www.penningtondoweaesthetics.co.uk</p>
  </div>
</section>

<section class="card card--back">
  <div class="accent-rule" style="left:0; width:147px; top:196px;"></div>
  <div class="accent-rule" style="left:539px; width:147px; top:196px;"></div>

  <div class="treatment-photo" role="img" aria-label="Collage photograph of a young woman's face and hands in soft monochrome tones"></div>

  <div class="services">
    <p>QUORVEX<span class="sep">|</span>LIP ENHANCEMENT<span class="sep">|</span>CHEMICAL PEELS</p>
    <p>FACIAL FILLERS<span class="sep">|</span>NON SURGICAL FACE LIFT</p>
  </div>
</section>

</body>
</html>
```